Brell Stone Company Business Cards

Front and Back Business Card - logo and text setup - cool design. I need workable photoshop or illustrator files so I can setup each employee card with design that is created
Updates

Hi everyone, thank you for the great entries. Please no more white and blue cards - there are so many already - black and silver only now please. thanks!

Target Market(s)

Construction Industry - Facility Managers

Industry/Entity Type

Construction

Contact Information for Business Card

I really like contemporary simplistic looks - clean neat....not opposed to seeing some black backrounds

Requirements
Must have
• Logo/website address with design on front only - www.brellstone-example.com (logo attached)
• Back:
• Name/Title/Company Address/Phone/email address
Nice to have
• Cool design
Should not have
• Nothing gimmicky like Fire or Water - since we are a Fire Protection company - it has all been done

```html
<!DOCTYPE html>
<html lang="en">
<head>
<meta charset="utf-8">
<title>Brell Stone Company – Business Cards</title>
<link rel="stylesheet" href="https://fonts.googleapis.com/css2?family=Roboto:wght@400;700;900&display=swap">
<style>
  :root {
    --backdrop: #1c1c1e;
    --card-black: #0d0d0e;
    --card-white: #ffffff;
    --silver: #8c8c8f;
    --silver-dim: #55555a;
    --accent: #ef4e2b;
    --accent-soft: #fbd9d0;
    --navy: #1f3470;
  }
  * { margin: 0; padding: 0; box-sizing: border-box; }
  html, body { width: 1200px; height: 800px; overflow: hidden; }
  body {
    background: var(--backdrop);
    font-family: "Roboto", Arial, sans-serif;
    display: flex;
    align-items: center;
    justify-content: center;
    gap: 40px;
  }
  .card {
    position: relative;
    width: 540px;
    height: 309px;
    border-radius: 2px;
    overflow: hidden;
  }
  /* Front */
  .card-front {
    background: var(--card-black);
    display: flex;
    flex-direction: column;
    align-items: center;
    justify-content: center;
    gap: 22px;
  }
  .brand-name {
    font-weight: 900;
    font-size: 54px;
    letter-spacing: -1px;
    color: var(--silver);
    line-height: 1;
  }
  .brand-web {
    font-size: 12px;
    letter-spacing: 5px;
    color: var(--silver-dim);
  }
  /* Back */
  .card-back { background: var(--card-white); }
  .band {
    position: absolute;
    height: 12px;
  }
  .band-left {
    left: 36px;
    width: 228px;
    background: linear-gradient(to right, var(--accent-soft), var(--accent));
  }
  .band-right {
    left: 306px;
    width: 198px;
    background: linear-gradient(to right, var(--accent), var(--accent-soft));
  }
  .band-top { top: 58px; }
  .band-bottom { top: 239px; }
  .identity {
    position: absolute;
    right: 275px;
    top: 128px;
    text-align: right;
  }
  .person-name {
    font-weight: 700;
    font-size: 24px;
    color: var(--navy);
    line-height: 1.1;
  }
  .person-title {
    font-size: 15px;
    color: var(--accent);
  }
  .divider {
    position: absolute;
    left: 280px;
    top: 98px;
    width: 1.5px;
    height: 114px;
    background: var(--accent);
  }
  .contacts {
    position: absolute;
    left: 296px;
    top: 111px;
    list-style: none;
    font-size: 12px;
    color: var(--navy);
    line-height: 22px;
  }
  .contacts li { display: flex; align-items: center; gap: 8px; white-space: nowrap; }
  .contacts svg { width: 11px; height: 11px; flex: none; }
  .contacts .web-domain { color: var(--accent); }
</style>
</head>
<body>
  <section class="card card-front" aria-label="Card front">
    <div class="brand-name">Brell Stone</div>
    <div class="brand-web">www.brellstone-example.com</div>
  </section>

  <section class="card card-back" aria-label="Card back">
    <div class="band band-left band-top" role="img" aria-label="Decorative accent band in orange tones"></div>
    <div class="band band-right band-top" role="img" aria-label="Decorative accent band in orange tones"></div>
    <div class="band band-left band-bottom" role="img" aria-label="Decorative accent band in orange tones"></div>
    <div class="band band-right band-bottom" role="img" aria-label="Decorative accent band in orange tones"></div>

    <div class="identity">
      <div class="person-name">Dana Whitlock</div>
      <div class="person-title">Director</div>
    </div>
    <div class="divider"></div>
    <ul class="contacts">
      <li>
        <svg viewBox="0 0 12 12"><rect x="2" y="1" width="8" height="10" rx="1.5" fill="none" stroke="var(--accent)" stroke-width="1.4"/></svg>
        (555) 014 2298
      </li>
      <li>
        <svg viewBox="0 0 12 12"><rect x="0.5" y="2.5" width="11" height="7" fill="var(--accent)"/><path d="M0.5 2.5 L6 6.5 L11.5 2.5" fill="none" stroke="#fff" stroke-width="1"/></svg>
        hello@brellstone-example.com
      </li>
      <li>
        <svg viewBox="0 0 12 12"><circle cx="6" cy="6" r="5.3" fill="var(--accent)"/><path d="M0.7 6 H11.3 M6 0.7 V11.3 M6 0.7 C3 3.5 3 8.5 6 11.3 M6 0.7 C9 3.5 9 8.5 6 11.3" fill="none" stroke="#fff" stroke-width="0.8"/></svg>
        <span>www.<span class="web-domain">brellstone-example</span>.com</span>
      </li>
      <li>
        <svg viewBox="0 0 12 12"><path d="M6 11.5 C3 7.8 1.8 6 1.8 4.4 A4.2 4.2 0 0 1 10.2 4.4 C10.2 6 9 7.8 6 11.5 Z" fill="var(--accent)"/><circle cx="6" cy="4.4" r="1.5" fill="#fff"/></svg>
        214 Harlow Avenue, Fairmont, CA 90210
      </li>
    </ul>
  </section>
</body>
</html>
```